依頼詳細
利用先は3パターンとなり、それぞれでデザインを作成して頂きます。
<利用先>
・ポスティング(A4)
・事務所壁に設置するポスター(B0サイズ)
・車両に貼付けするマグネットシート(縦横30cm幅でバンの後ろに取付)※左右2枚に分けてか1枚に収まるでも可
記載項目
社名、求人条件https://jp.shigotomadoguchi.net/q-%E9%9B%BB%E6%B0%97%E5%B7%A5%E4%BA%8B%E5%A3%AB-l-%E5%85%B5%E5%BA%AB%E7%9C%8C-%E5%8A%A0%E5%8F%A4%E5%B7%9D%E5%B8%82-%E6%B1%82%E4%BA%BA.html?vjk=3f91c2b7d05e6a48&advn=2739481650274813

別途添付資料の分析表
サイズ
ポスティングA4、ポスターB0、マグネットシート縦横30cm
ページ数
片面
希望イメージ
シンプル 複雑
単色 カラフル
暗い 明るい
日常 高級
遊び心 厳粛
未来的 伝統的
女性的 男性的
希望する色
緑系、水色系
納品ファイル
• イラストレーター形式 (.ai)
補足説明

メッセージではご連絡させていただいておりましたが、非常にわかりやすいデザインで目が惹かれました。
よろしくお願いいたします。

この度はご提案いただき誠にありがとうございました。
皆さん非常に目の惹かれるデザインでしたが、社内にて検討の結果選定させていただきました。

また、今後依頼させていただくことも増える予定ですので機会がございましたらその際はよろしくお願いいたします。

```html
<!DOCTYPE html>
<html lang="ja">
<head>
<meta charset="utf-8">
<title>電気工事士 正社員募集</title>
<link href="https://fonts.googleapis.com/css2?family=Noto+Sans+JP:wght@400;500;700;900&family=Zen+Kaku+Gothic+New:wght@700;900&display=swap" rel="stylesheet">
<style>
:root{
  --blue:#1b4f9c;
  --blue-dark:#143a76;
  --green:#57b230;
  --green-light:#e7f4de;
  --sky:#e6f2fb;
  --ink:#2a2a2a;
  --white:#ffffff;
}
*{box-sizing:border-box;margin:0;padding:0}
html,body{width:849px;height:1200px;overflow:hidden;background:var(--white)}
body{font-family:"Noto Sans JP",sans-serif;color:var(--ink)}
.poster{position:relative;width:849px;height:1200px;background:var(--white);overflow:hidden}
.hero-photo{position:absolute;right:0;top:0;width:500px;height:560px;
  background:linear-gradient(180deg,#9cc8e6 0%,#d9ebf6 45%,#c9d5df 70%,#e9eef2 100%)}
.hero-fade{position:absolute;left:300px;top:0;width:220px;height:560px;background:linear-gradient(90deg,#fff,rgba(255,255,255,0))}
.lead{position:absolute;left:38px;top:30px}
.lead .line1{display:inline-block;background:var(--green);color:var(--white);font-family:"Zen Kaku Gothic New",sans-serif;font-weight:900;font-size:38px;padding:2px 14px;transform:skewX(-6deg)}
.lead .line2{display:inline-block;margin-top:8px;background:var(--white);border:3px solid var(--blue);color:var(--blue);font-family:"Zen Kaku Gothic New",sans-serif;font-weight:900;font-size:38px;padding:0 12px}
.vertical{position:absolute;right:40px;top:26px;writing-mode:vertical-rl;font-weight:900;font-size:24px;color:var(--white);
  text-shadow:0 0 4px var(--green),0 0 4px var(--green),0 0 4px var(--green);line-height:1.25}
.title{position:absolute;left:38px;top:175px;font-family:"Zen Kaku Gothic New",sans-serif;font-weight:900;color:var(--blue);line-height:1.05}
.title .t1{font-size:72px;letter-spacing:2px}
.title .t2{font-size:72px;letter-spacing:2px;background:linear-gradient(transparent 62%,#cdeab9 62%)}
.salary{position:absolute;left:40px;top:345px;font-weight:900;color:var(--blue);font-size:30px}
.salary b{font-size:52px;letter-spacing:1px}
.features{position:absolute;left:40px;top:430px;color:var(--green);font-weight:900;font-size:24px;line-height:1.4}
.station{position:absolute;left:538px;top:430px;width:122px;height:122px;border-radius:50%;background:var(--blue);color:var(--white);
  display:flex;flex-direction:column;align-items:center;justify-content:center;font-weight:900;font-size:22px;line-height:1.2;border:4px solid var(--white);box-shadow:0 0 0 3px var(--blue)}
.station span{font-size:26px}
.info{position:absolute;left:0;top:560px;width:849px;height:520px;background:var(--sky)}
.card{position:absolute;top:590px;width:370px;height:150px;background:var(--white);border:2px solid var(--blue);border-radius:10px;text-align:center;padding-top:34px}
.card .label{position:absolute;left:50%;top:-16px;transform:translateX(-50%);background:var(--blue);color:var(--white);font-weight:700;font-size:17px;padding:4px 28px;border-radius:20px;white-space:nowrap}
.card .main{font-weight:900;font-size:20px;color:var(--blue);line-height:1.45}
.card .sub{font-size:13px;margin-top:6px;line-height:1.5}
.card.job{left:38px}
.card.req{left:440px}
.points{position:absolute;left:38px;top:765px;width:360px}
.point{display:flex;gap:12px;margin-bottom:16px}
.point .num{color:var(--green);font-weight:900;font-size:15px;line-height:1;text-align:center;width:54px}
.point .num b{display:block;font-size:38px;color:var(--blue)}
.point p{font-size:15px;font-weight:700;line-height:1.5;padding-top:4px}
.details{position:absolute;left:430px;top:765px;width:385px;border-collapse:collapse;font-size:12px}
.details th{width:78px;background:var(--blue);color:var(--white);font-weight:700;padding:6px 4px;border-bottom:2px solid var(--sky);white-space:nowrap}
.details td{background:var(--white);padding:6px 8px;border-bottom:2px solid var(--sky);line-height:1.4}
.notice{position:absolute;left:0;top:1032px;width:849px;text-align:center;color:var(--green);font-weight:900;font-size:21px}
.footer{position:absolute;left:0;top:1080px;width:849px;height:120px;background:var(--white);border-top:4px solid var(--green)}
.brand{position:absolute;left:38px;top:20px;display:flex;align-items:center;gap:10px}
.brand .mark{width:42px;height:42px;border-radius:50%;background:var(--green)}
.brand .name{font-weight:900;font-size:30px;color:var(--blue)}
.brand small{display:block;font-size:11px;font-weight:700;color:var(--blue)}
.address{position:absolute;left:38px;top:80px;font-size:12px}
.contact{position:absolute;left:380px;top:14px}
.phone{display:flex;align-items:center;gap:8px;color:var(--blue);font-weight:900;font-size:42px;letter-spacing:1px}
.phone .icon{width:44px;height:44px;border-radius:50%;background:var(--green);display:flex;align-items:center;justify-content:center}
.web{margin-top:8px;display:flex;align-items:center;gap:10px}
.web .url{font-weight:700;font-size:17px;color:var(--blue)}
.web .apply{background:var(--blue);color:var(--white);font-weight:700;font-size:15px;padding:5px 16px;border-radius:4px}
</style>
</head>
<body>
<main class="poster">
  <div class="hero-photo" role="img" aria-label="ヘルメット姿の作業員と太陽光パネルの写真"></div>
  <div class="hero-fade"></div>

  <div class="lead">
    <div class="line1">僕たちと一緒に</div><br>
    <div class="line2">地域貢献しませんか?</div>
  </div>
  <div class="vertical">資格取得支援あり<br>年2日制でプライベートも充実</div>

  <h1 class="title"><div class="t1">電気工事士</div><div class="t2">正社員募集</div></h1>
  <div class="salary">月給 <b>28～40</b>万円</div>
  <div class="features">学歴不問！業界未経験OK！<br>異業種からの転職OK！ブランクOK！</div>
  <div class="station"><div>南浜駅</div><div>から</div><span>徒歩7分</span></div>

  <section class="info"></section>
  <div class="card job">
    <div class="label">仕事内容</div>
    <div class="main">太陽光に関わる電気工事全般</div>
    <div class="sub">その他 Q8改造・電灯線路・硬性・行政防災<br>無線工事・通信工事・各種電気工事全般</div>
  </div>
  <div class="card req">
    <div class="label">必須条件</div>
    <div class="main">第一種または<br>第二種電気工事士をお持ちの方<br>電気工事の実務経験がある方</div>
  </div>

  <div class="points">
    <div class="point"><div class="num">Point<b>01</b></div><p>社員同士はもちろん、他部署とのつながりも強く業務がスムーズに進む！</p></div>
    <div class="point"><div class="num">Point<b>02</b></div><p>仕事への姿勢を正当に評価する風土が根付いています！</p></div>
    <div class="point"><div class="num">Point<b>03</b></div><p>社歴や年齢に関係なくスピード感のあるキャリアアップが可能！</p></div>
  </div>

  <table class="details">
    <tr><th>勤務地</th><td>〒675-0000 兵庫県加古川市南町1-2-3<br>マイカー・バイク・自転車通勤OK</td></tr>
    <tr><th>勤務時間</th><td>8:00～17:00 季節や現場により変動あり</td></tr>
    <tr><th>休日</th><td>土曜・日曜・祝日（工期により出勤あり）</td></tr>
    <tr><th>試用期間</th><td>3ヶ月（期間中の条件変更なし）</td></tr>
    <tr><th>休暇</th><td>年間休日120日以上・GW・夏季・年末年始</td></tr>
    <tr><th>福利厚生</th><td>社会保険完備・資格取得支援・交通費支給<br>退職金制度・作業服貸与・健康診断</td></tr>
  </table>

  <div class="notice">給料・賞与は年2回。ライフステージの変化にも左右されず、長く働ける安心の環境！</div>

  <footer class="footer">
    <div class="brand">
      <div class="mark"></div>
      <div class="name"><small>太陽光発電施工 株式会社</small>ソラテック</div>
    </div>
    <div class="address">兵庫県加古川市南町1-2-3</div>
    <div class="contact">
      <div class="phone">
        <span class="icon"><svg width="24" height="24" viewBox="0 0 24 24"><path fill="#fff" d="M6.6 10.8c1.4 2.8 3.8 5.1 6.6 6.6l2.2-2.2c.3-.3.7-.4 1-.2 1.1.4 2.3.6 3.6.6.6 0 1 .4 1 1V20c0 .6-.4 1-1 1C10.6 21 3 13.4 3 4c0-.6.4-1 1-1h3.5c.6 0 1 .4 1 1 0 1.3.2 2.5.6 3.6.1.3 0 .7-.2 1z"/></svg></span>
        079-000-4821
      </div>
      <div class="web"><span class="url">soratec-works.jp</span><span class="apply">採用応募フォームはこちら</span></div>
    </div>
  </footer>
</main>
</body>
</html>
```